Creative/Kindred law firm website

A law firm website that immediately looks different from other law firm websites. We like the color scheme (dark background with warm, neutral colors) and simple, organic logos (trees, leaves, etc.) of this website: https://brambleworth.legal/

We'll be offering creative/innovative solutions to complex problems faced by state governments, industries, other law firms, and individuals. We're located in Montana (U.S.A.), and the outdoors is a huge part of our lives and identities.

We will need a home page, an "About Us" page with a separate subpage for each attorney (two attorneys), a blog or "Publications" page, a payment portal (which will integrate with Quillo), and a "Services" page.

```html
<!DOCTYPE html>
<html lang="en">
<head>
<meta charset="utf-8">
<title>Kindred law</title>
<link href="https://fonts.googleapis.com/css2?family=Lato:ital,wght@0,400;0,700;0,900;1,400&display=swap" rel="stylesheet">
<style>
:root{
  --dark:#2e1217;
  --dark-2:#4f1e26;
  --wine:#4f1b25;
  --plum:#5a232b;
  --mauve:#8c5c5c;
  --rose:#b9766a;
  --title:#8b4a4a;
  --sand:#c9aca4;
  --cream:#e9dcd7;
  --orange:#c87a44;
  --footer-head:#d08a55;
  --white:#ffffff;
  --ink:#222222;
}
*{margin:0;padding:0;box-sizing:border-box}
html,body{width:1200px;height:3518px;overflow:hidden}
body{position:relative;background:var(--dark);font-family:'Lato',sans-serif;color:var(--ink)}
.abs{position:absolute}
.backdrop{position:absolute;left:0;top:0}
.hero-photo{position:absolute;left:0;top:0;width:1200px;height:640px;background:radial-gradient(ellipse at 70% 30%,#4a2a33 0%,#33161d 45%,#220b10 100%)}
.logo{left:88px;top:20px;font-size:27px;font-weight:700;color:var(--white)}
.nav{top:27px;font-size:14px;color:var(--cream)}
.nav.active{text-decoration:underline}
.btn{position:absolute;display:flex;align-items:center;justify-content:center;font-size:14px;font-weight:700;border-radius:3px}
.btn-inquiry{left:976px;top:19px;width:136px;height:36px;background:#7a3b47;color:var(--cream)}
.hero-kicker{left:88px;top:184px;font-size:21px;font-weight:700;color:var(--cream)}
.hero-title{left:88px;top:220px;font-size:33px;font-weight:900;line-height:38px;color:var(--rose)}
.btn-sand{background:var(--sand);color:var(--wine)}
.btn-wine{background:var(--wine);color:var(--cream)}
.section-title{font-size:33px;font-weight:900;color:var(--title)}
.about-lead{left:146px;top:697px;width:380px;font-size:14px;font-weight:700;line-height:19px;color:#111}
.about-copy{left:146px;width:460px;font-size:14px;line-height:19px;color:#222}
.photo-ring{position:absolute;border-radius:50%;border:2px solid var(--mauve)}
.photo{position:absolute;border-radius:50%}
.service{position:absolute;border-radius:50%;background:var(--plum);display:flex;flex-direction:column;align-items:center;text-align:center;color:var(--cream)}
.service.featured{border:8px solid var(--orange)}
.service svg{margin-top:46px}
.service h3{font-size:18px;font-weight:700;margin-top:12px}
.service p{font-size:11.5px;line-height:15px;width:200px;margin-top:8px;color:#dcc8c2}
.card{position:absolute;background:var(--white);box-shadow:0 2px 14px rgba(0,0,0,.12);border-radius:2px}
.attorney-name{font-size:21px;font-weight:700;color:var(--wine)}
.attorney-role{font-size:14px;color:#8a5a50}
.attorney-bio{font-size:14px;line-height:19px;color:#333;width:245px}
.blog-card{position:absolute;width:325px;height:311px;border-radius:14px;overflow:hidden;background:var(--dark-2)}
.blog-card.light{background:var(--sand)}
.blog-img{height:173px;width:100%}
.blog-arrow{position:absolute;left:270px;top:157px;width:36px;height:36px;border-radius:50%;background:var(--cream);display:flex;align-items:center;justify-content:center}
.blog-card.light .blog-arrow{background:var(--wine)}
.blog-meta{position:absolute;left:24px;top:193px;display:flex;gap:14px;color:var(--cream)}
.blog-date{font-size:12px;font-weight:700;line-height:15px}
.blog-by{font-size:12px;font-style:italic;line-height:15px}
.blog-text{position:absolute;left:24px;top:242px;width:240px;font-size:15px;line-height:21px;color:var(--cream)}
.blog-card.light .blog-meta,.blog-card.light .blog-text{color:var(--wine)}
.btn-view{left:1008px;top:2167px;width:104px;height:30px;background:#6a2d36;color:var(--cream);font-weight:400;font-size:14px;gap:6px}
.field{position:absolute;border:1px solid #d9d0cd;background:var(--white);display:flex;align-items:center;gap:8px;padding-left:12px;font-size:12px;color:#777}
.field.area{align-items:flex-start;padding-top:11px}
.foot-head{font-size:20px;font-weight:700;color:var(--footer-head)}
.foot-label{font-size:14px;color:#a98d88}
.foot-text{font-size:14px;color:var(--cream);line-height:20px}
.foot-link{left:442px;font-size:14px;color:var(--cream)}
.social{position:absolute;width:10px;height:10px;border-radius:50%;background:var(--cream);top:3408px}
.copyright{left:0;top:3475px;width:1200px;height:43px;background:var(--mauve);display:flex;align-items:center;justify-content:center;font-size:14px;color:var(--cream)}
</style>
</head>
<body>

<div class="hero-photo" role="img" aria-label="Dark wine-toned photo of justice scales and digital legal icons"></div>

<svg class="backdrop" width="1200" height="3518" viewBox="0 0 1200 3518" aria-hidden="true">
  <path fill="#8c5c5c" d="M0,555 C300,470 520,425 720,430 C920,435 1100,470 1200,465 L1200,530 L1200,1000 C1000,1060 800,1082 600,1077 C340,1070 150,1010 0,1000 Z"/>
  <path fill="#ffffff" d="M0,610 C300,520 520,432 720,438 C920,444 1100,490 1200,528 L1200,945 C1000,1040 800,1078 600,1075 C350,1070 150,990 0,935 Z"/>
  <path fill="#8c5c5c" d="M0,1575 C250,1500 450,1470 620,1470 C850,1472 1050,1470 1200,1470 L1200,1565 L1200,1965 C1000,2040 800,2090 600,2088 C350,2085 150,2020 0,2010 Z"/>
  <path fill="#ffffff" d="M0,1575 C250,1505 450,1470 620,1470 C850,1472 1050,1500 1200,1565 L1200,1965 C1000,2030 800,2088 600,2088 C350,2086 150,2010 0,1950 Z"/>
  <path fill="#8c5c5c" d="M0,2740 C250,2670 450,2628 620,2628 C850,2630 1050,2628 1200,2630 L1200,2710 L1200,3020 C1000,3060 800,3082 600,3080 C350,3078 150,3025 0,3015 Z"/>
  <path fill="#ffffff" d="M0,2740 C250,2670 450,2628 620,2628 C850,2630 1050,2650 1200,2710 L1200,3020 C1000,3050 800,3080 600,3080 C350,3078 150,3005 0,2955 Z"/>
</svg>

<div class="abs logo">Kindred law</div>
<div class="abs nav active" style="left:444px">Home</div>
<div class="abs nav" style="left:512px">About Us</div>
<div class="abs nav" style="left:601px">Services</div>
<div class="abs nav" style="left:682px">Our Attorney</div>
<div class="abs nav" style="left:797px">Blogs</div>
<div class="abs nav" style="left:865px">Contact Us</div>
<div class="btn btn-inquiry">Quick Inquiry</div>

<div class="abs hero-kicker">We Make Difference</div>
<div class="abs hero-title">Our Firm Offers a Wide Range<br>of Legal Services</div>
<div class="btn btn-sand" style="left:88px;top:332px;width:137px;height:39px">Learn More</div>

<div class="abs section-title" style="left:146px;top:627px">About Us</div>
<div class="abs about-lead">Lorem Ipsum is simply dummy text of the printing and typesetting industry.</div>
<div class="abs about-copy" style="top:754px">Lorem Ipsum has been the industry's standard dummy text ever since the 1500s, when an unknown printer took a galley of type and scrambled it to make a type specimen book.</div>
<div class="abs about-copy" style="top:831px">It has survived not only five centuries, but also the leap into electronic typesetting, remaining essentially unchanged.</div>
<div class="btn btn-wine" style="left:146px;top:904px;width:137px;height:39px">Learn More</div>
<div class="photo-ring" style="left:707px;top:585px;width:366px;height:360px"></div>
<div class="photo" role="img" aria-label="Team of lawyers meeting around a wooden table with documents" style="left:718px;top:590px;width:352px;height:352px;background:radial-gradient(circle at 60% 40%,#c9a57e 0%,#8f7a6c 50%,#5c5860 100%)"></div>

<div class="service" style="left:174px;top:1151px;width:240px;height:240px">
  <svg width="48" height="48" viewBox="0 0 48 48"><path fill="#c87a44" d="M42,4 C20,6 6,16 8,36 L4,44 L8,44 L11,38 C32,40 42,26 42,4 Z"/></svg>
  <h3>Solo / Small Firm</h3>
  <p>Lorem Ipsum is simply dummy text of the printing and typesetting industry.</p>
</div>
<div class="service" style="left:480px;top:1151px;width:240px;height:240px">
  <svg width="48" height="60" viewBox="0 0 48 60" style="margin-top:40px"><g fill="#c87a44"><path d="M23,58 C26,44 26,30 24,4 L27,4 C29,30 29,44 26,58 Z"/><ellipse cx="25" cy="10" rx="5" ry="9"/><ellipse cx="14" cy="26" rx="10" ry="5" transform="rotate(25 14 26)"/><ellipse cx="36" cy="24" rx="10" ry="5" transform="rotate(-25 36 24)"/><ellipse cx="12" cy="42" rx="11" ry="5" transform="rotate(20 12 42)"/><ellipse cx="38" cy="40" rx="11" ry="5" transform="rotate(-20 38 40)"/></g></svg>
  <h3 style="margin-top:6px">Mid size Firm</h3>
  <p>Lorem Ipsum is simply dummy text of the printing and typesetting industry.</p>
</div>
<div class="service featured" style="left:775px;top:1141px;width:260px;height:260px">
  <svg width="56" height="60" viewBox="0 0 56 60" style="margin-top:42px"><g fill="#c87a44"><path d="M25,58 L26,28 L30,28 L31,58 Z"/><path d="M27,36 L14,24 L16,22 L28,33 Z"/><path d="M29,36 L42,24 L40,22 L28,33 Z"/><circle cx="28" cy="8" r="5"/><circle cx="16" cy="14" r="5"/><circle cx="40" cy="14" r="5"/><circle cx="10" cy="24" r="4"/><circle cx="46" cy="24" r="4"/><circle cx="22" cy="20" r="4"/><circle cx="34" cy="20" r="4"/></g></svg>
  <h3 style="margin-top:6px">Large Firm</h3>
  <p>Lorem Ipsum is simply dummy text of the printing and typesetting industry.</p>
</div>

<div class="abs section-title" style="left:0;width:1200px;text-align:center;top:1558px">Our Attorney</div>

<div class="card" style="left:185px;top:1647px;width:399px;height:275px"></div>
<div class="photo-ring" style="left:95px;top:1677px;width:200px;height:198px"></div>
<div class="photo" role="img" aria-label="Portrait photo of attorney Wade Hollister" style="left:103px;top:1680px;width:192px;height:192px;background:radial-gradient(circle at 50% 40%,#c8a08a 0%,#8a6d62 45%,#3b3437 100%)"></div>
<div class="abs attorney-name" style="left:318px;top:1675px">Wade Hollister</div>
<div class="abs attorney-role" style="left:318px;top:1700px">Lawyer</div>
<div class="abs attorney-bio" style="left:318px;top:1734px">Lorem Ipsum has been the industry's standard dummy text ever since the 1500s, when an unknown printer took a galley of type and scrambled it to make a type specimen book.</div>
<div class="btn btn-sand" style="left:318px;top:1858px;width:97px;height:33px;font-weight:400;color:var(--wine)">More</div>

<div class="card" style="left:710px;top:1647px;width:399px;height:275px"></div>
<div class="photo-ring" style="left:621px;top:1677px;width:200px;height:198px"></div>
<div class="photo" role="img" aria-label="Portrait photo of attorney Callum Reyes" style="left:629px;top:1680px;width:192px;height:192px;background:radial-gradient(circle at 50% 40%,#d2b09c 0%,#8f7c74 45%,#4a4a4e 100%)"></div>
<div class="abs attorney-name" style="left:843px;top:1675px">Callum Reyes</div>
<div class="abs attorney-role" style="left:843px;top:1700px">Lawyer</div>
<div class="abs attorney-bio" style="left:843px;top:1734px">Lorem Ipsum has been the industry's standard dummy text ever since the 1500s, when an unknown printer took a galley of type and scrambled it to make a type specimen book.</div>
<div class="btn btn-wine" style="left:843px;top:1858px;width:97px;height:33px;font-weight:400">More</div>

<div class="abs section-title" style="left:0;width:1200px;text-align:center;top:2158px;color:var(--sand)">Our Blogs</div>
<div class="btn btn-view">View All
  <svg width="12" height="12" viewBox="0 0 12 12"><path d="M1,6 H10 M6,2 L10,6 L6,10" stroke="#e9dcd7" stroke-width="1.6" fill="none"/></svg>
</div>

<div class="blog-card" style="left:88px;top:2239px">
  <div class="blog-img" role="img" aria-label="Photo of a judge's gavel and scales beside a laptop" style="background:linear-gradient(135deg,#e8e0d6 0%,#b79a82 55%,#5b3a2a 100%)"></div>
  <div class="blog-arrow"><svg width="18" height="18" viewBox="0 0 18 18"><path d="M2,9 H15 M9,3 L15,9 L9,15" stroke="#4f1b25" stroke-width="2.2" fill="none"/></svg></div>
  <div class="blog-meta"><svg width="22" height="22" viewBox="0 0 22 22"><rect x="2" y="4" width="18" height="16" rx="2" fill="none" stroke="#e9dcd7" stroke-width="1.6"/><path d="M2,9 H20 M7,2 V6 M15,2 V6" stroke="#e9dcd7" stroke-width="1.6"/></svg><div><div class="blog-date">Dec 06, 2021</div><div class="blog-by">by Ellis Marsh</div></div></div>
  <div class="blog-text">Lorem Ipsum is simply dummy text of typesetting industry.</div>
</div>

<div class="blog-card" style="left:437px;top:2239px">
  <div class="blog-img" role="img" aria-label="Photo of a hand touching glowing legal icons on a blue hexagon grid" style="background:linear-gradient(135deg,#bcd3e6 0%,#3d74b0 50%,#163b6b 100%)"></div>
  <div class="blog-arrow"><svg width="18" height="18" viewBox="0 0 18 18"><path d="M2,9 H15 M9,3 L15,9 L9,15" stroke="#4f1b25" stroke-width="2.2" fill="none"/></svg></div>
  <div class="blog-meta"><svg width="22" height="22" viewBox="0 0 22 22"><rect x="2" y="4" width="18" height="16" rx="2" fill="none" stroke="#e9dcd7" stroke-width="1.6"/><path d="M2,9 H20 M7,2 V6 M15,2 V6" stroke="#e9dcd7" stroke-width="1.6"/></svg><div><div class="blog-date">Dec 06, 2021</div><div class="blog-by">by Ellis Marsh</div></div></div>
  <div class="blog-text">Lorem Ipsum is simply dummy text of typesetting industry.</div>
</div>

<div class="blog-card light" style="left:787px;top:2239px">
  <div class="blog-img" role="img" aria-label="Photo of two businesspeople shaking hands over a desk" style="background:linear-gradient(135deg,#d9d6d4 0%,#6f6a69 50%,#2a2626 100%)"></div>
  <div class="blog-arrow"><svg width="18" height="18" viewBox="0 0 18 18"><path d="M2,9 H15 M9,3 L15,9 L9,15" stroke="#e9dcd7" stroke-width="2.2" fill="none"/></svg></div>
  <div class="blog-meta"><svg width="22" height="22" viewBox="0 0 22 22"><rect x="2" y="4" width="18" height="16" rx="2" fill="none" stroke="#4f1b25" stroke-width="1.6"/><path d="M2,9 H20 M7,2 V6 M15,2 V6" stroke="#4f1b25" stroke-width="1.6"/></svg><div><div class="blog-date">Dec 06, 2021</div><div class="blog-by">by Ellis Marsh</div></div></div>
  <div class="blog-text">Lorem Ipsum is simply dummy text of typesetting industry.</div>
</div>

<div class="abs section-title" style="left:0;width:1200px;text-align:center;top:2712px;color:var(--wine)">Quick Inquiry</div>
<div class="field" style="left:124px;top:2786px;width:308px;height:39px"><svg width="14" height="14" viewBox="0 0 14 14"><circle cx="7" cy="4" r="3" fill="none" stroke="#555" stroke-width="1.3"/><path d="M1,13 C1,8 13,8 13,13" fill="none" stroke="#555" stroke-width="1.3"/></svg>Name</div>
<div class="field" style="left:446px;top:2786px;width:308px;height:39px"><svg width="14" height="12" viewBox="0 0 14 12"><rect x="1" y="1" width="12" height="10" fill="none" stroke="#555" stroke-width="1.3"/><path d="M1,1 L7,6 L13,1" fill="none" stroke="#555" stroke-width="1.3"/></svg>Email</div>
<div class="field" style="left:768px;top:2786px;width:308px;height:39px"><svg width="10" height="14" viewBox="0 0 10 14"><rect x="1" y="1" width="8" height="12" rx="1.5" fill="none" stroke="#555" stroke-width="1.3"/></svg>Phone</div>
<div class="field area" style="left:124px;top:2840px;width:952px;height:108px"><svg width="13" height="13" viewBox="0 0 13 13"><path d="M1,1 H12 V8 L8,12 H1 Z" fill="none" stroke="#555" stroke-width="1.3"/></svg>How can we help?</div>
<div class="btn btn-sand" style="left:543px;top:2988px;width:114px;height:39px;color:var(--wine)">Submit</div>

<div class="photo-ring" style="left:700px;top:3052px;width:394px;height:390px"></div>
<div class="photo" role="img" aria-label="Grey street map showing the office location" style="left:712px;top:3058px;width:380px;height:380px;background:radial-gradient(circle at 45% 50%,#f0f0f0 0%,#dcdcdc 60%,#c4c4c4 100%)"></div>

<div class="abs foot-head" style="left:88px;top:3180px">Conatct Info</div>
<div class="abs" style="left:88px;top:3228px;font-size:18px;color:var(--cream)"><span style="font-size:13px;color:var(--rose)">Call Us:</span> +44 (0) 1632 960418</div>
<div class="abs foot-text" style="left:88px;top:3256px">hello@kindredlaw-studio.com</div>
<div class="abs foot-label" style="left:88px;top:3292px">Address:</div>
<div class="abs foot-text" style="left:88px;top:3315px">4 Larchwood Mews,<br>Ferngate Hollow</div>
<div class="abs foot-label" style="left:88px;top:3375px">Social Media:</div>
<div class="social" style="left:89px"></div>
<div class="social" style="left:117px"></div>
<div class="social" style="left:147px"></div>
<div class="social" style="left:178px"></div>

<div class="abs foot-head" style="left:440px;top:3180px">Quick Links</div>
<div class="abs foot-link" style="top:3228px;text-decoration:underline">Home</div>
<div class="abs foot-link" style="top:3259px">About Us</div>
<div class="abs foot-link" style="top:3290px">Services</div>
<div class="abs foot-link" style="top:3322px">Our Attorney</div>
<div class="abs foot-link" style="top:3353px">Blogs</div>
<div class="abs foot-link" style="top:3384px">Contact Us</div>

<div class="abs copyright">Copyright © Kindred law. All Rights Reserved</div>

</body>
</html>
```